I work in creative/artistic projects across different mediums.
It needs to communicate creativity, style, sexy, uniqueness, individuality and sophistication.
It should not look corporate.
Colours I like are black silver gold deep purple, chocolate, orchid.
It doesn't have to make use of all these colours.
I do not like bright primary colors.
Updates

Project Deadline Extended
Reason: Still in the communication process and to allow the person enough time to finish the design. Though i should know in the next day or two. Thank you.

Target Market(s)

creatives and companies wanting to inject creativity into thier business.

Industry/Entity Type

Work

Contact Information for Business Card

Lionel Crowthwick
0418359026
lionel@lionelcrowthwick.com

quietsilverhour.com.au

Requirements
Should not have
• Anything corporate OR OLD FASHIONED

```html
<!DOCTYPE html>
<html lang="en">
<head>
<meta charset="utf-8">
<title>Lionel Crowthwick — Business Card</title>
<link rel="stylesheet" href="https://fonts.googleapis.com/css2?family=Indie+Flower&family=Gloria+Hallelujah&display=swap">
<style>
  :root {
    --night-deep: #141a24;
    --night-mid: #2c3a4e;
    --night-light: #4a5e78;
    --gold: #e2b006;
    --ink-white: #ffffff;
  }
  html, body {
    margin: 0;
    padding: 0;
    width: 1200px;
    height: 742px;
    overflow: hidden;
    background: var(--night-deep);
  }
  .card {
    position: relative;
    width: 1200px;
    height: 742px;
    overflow: hidden;
  }
  .card__texture {
    position: absolute;
    inset: 0;
    background:
      radial-gradient(ellipse at 30% 30%, rgba(90,110,140,0.45), transparent 60%),
      linear-gradient(160deg, var(--night-light) 0%, var(--night-mid) 45%, var(--night-deep) 100%);
  }
  .name-band {
    position: absolute;
    left: 282px;
    top: 56px;
    width: 902px;
    height: 139px;
    background: var(--gold);
  }
  .name-band__name {
    position: absolute;
    right: 40px;
    top: 50%;
    transform: translateY(-52%);
    margin: 0;
    font-family: "Gloria Hallelujah", "Indie Flower", cursive;
    font-weight: 400;
    font-size: 66px;
    line-height: 1;
    color: var(--ink-white);
    white-space: nowrap;
  }
  .contact {
    position: absolute;
    right: 54px;
    top: 380px;
    margin: 0;
    padding: 0;
    list-style: none;
    text-align: right;
    font-family: "Indie Flower", cursive;
    font-size: 58px;
    line-height: 111px;
    color: var(--gold);
  }
  .contact__item { white-space: nowrap; }
</style>
</head>
<body>
  <main class="card">
    <div class="card__texture" role="img" aria-label="Dark blue grunge texture of overlapping translucent painted strokes"></div>
    <header class="name-band">
      <h1 class="name-band__name">Lionel Crowthwick</h1>
    </header>
    <ul class="contact">
      <li class="contact__item contact__phone">0418359026</li>
      <li class="contact__item contact__email">lionel@lionelcrowthwick.com</li>
      <li class="contact__item contact__web">quietsilverhour.com.au</li>
    </ul>
  </main>
</body>
</html>
```